Menu Design Project

We trying to replace old flyer/menu with some new design.
hello this is my old menu i attached in email and my logo, the text you can pick from the menu and and i also attached some new picture for the food ,with my menu size unfold. front and back and then fold to 3.5" * 11". please show me what best can you do .Trifold is fine but must have image of food,
this is indian Restaurant
thats fine to have trifold menu design do to short time

Need to add also food picture on menu

Font styles to use
Serif
Decorative
Script

Colors

Designer to choose colors to be used in the design.

Requirements
Must have
• food image on menu
• trifold is fine ( do to short time)
• menu has to elegant ,color or text can be optional, Menu need to be neat and clean no too much rush on between the words .

```html
<!DOCTYPE html>
<html lang="en">
<head>
<meta charset="utf-8">
<title>Indian Restaurant Trifold Menu</title>
<link rel="stylesheet" href="https://fonts.googleapis.com/css2?family=Oswald:wght@400;500&family=Roboto+Condensed:wght@400&display=swap">
<style>
  :root {
    --navy: #101d3c;
    --navy-light: #1d3766;
    --panel: #050505;
    --gold: #f4d23c;
    --price: #f2f2f2;
    --desc: #d9d9d9;
    --food-warm: #b5652a;
    --food-dark: #3b2a22;
  }
  * { margin: 0; padding: 0; box-sizing: border-box; }
  html, body { width: 1145px; height: 1200px; overflow: hidden; background: var(--navy); }
  .menu { position: relative; width: 1145px; height: 1200px; overflow: hidden; }
  .backdrop { position: absolute; inset: 0; background: radial-gradient(circle at 50% 40%, var(--navy-light), var(--navy) 70%); }
  .panels { position: absolute; inset: 0; }
  .section-title {
    position: absolute; text-align: center; color: var(--gold);
    font-family: "Oswald", sans-serif; font-weight: 500; font-size: 23px; line-height: 1.05;
    letter-spacing: 0.3px; text-transform: uppercase;
  }
  .divider { position: absolute; height: 1px; width: 52px; background: #e8e8e8; }
  .divider::after { content: ""; position: absolute; left: 22px; top: -3px; width: 7px; height: 7px; border: 1px solid #e8e8e8; transform: rotate(45deg); background: var(--panel); }
  .menu-list { position: absolute; list-style: none; }
  .item { height: var(--row); }
  .item-line { display: flex; align-items: baseline; font-family: "Oswald", sans-serif; font-size: 11.5px; line-height: 14px; color: var(--gold); text-transform: uppercase; white-space: nowrap; }
  .leader { flex: 1; margin: 0 4px; border-bottom: 2px dotted var(--gold); transform: translateY(-3px); }
  .price { color: var(--price); font-size: 11px; }
  .desc { font-family: "Roboto Condensed", sans-serif; font-size: 6.3px; line-height: 8px; color: var(--desc); padding-left: 18px; white-space: nowrap; overflow: hidden; }
  .food-photo { position: absolute; left: 382px; top: 428px; width: 381px; height: 286px; border-radius: 40px;
    background: radial-gradient(ellipse at 50% 50%, var(--food-warm), var(--food-dark) 75%, var(--panel)); }
</style>
</head>
<body>
<main class="menu">
  <div class="backdrop" role="img" aria-label="Dark navy damask pattern background"></div>

  <svg class="panels" width="1145" height="1200" viewBox="0 0 1145 1200" aria-hidden="true">
    <path d="M22 1188 L22 100 C22 62 120 52 196 22 C272 52 370 62 370 100 L370 1188 Z" fill="#050505"/>
    <rect x="382" y="0" width="381" height="1200" fill="#050505"/>
    <path d="M763 1188 L763 100 C763 62 866 52 942 22 C1018 52 1122 62 1122 100 L1122 1188 Z" fill="#050505"/>
  </svg>

  <!-- Left panel -->
  <h2 class="section-title" style="left:22px;width:348px;top:96px;">Non- Vegetarian<br>Appetizer</h2>
  <div class="divider" style="left:170px;top:160px;"></div>
  <ul class="menu-list" style="left:50px;width:296px;top:182px;--row:27.2px;">
    <li class="item"><div class="item-line">Chicken Samosa<span class="leader"></span><span class="price">$6.99</span></div><p class="desc">spicy chicken keema with peas wrapped in alight pastry</p></li>
    <li class="item"><div class="item-line">Chicken Pakora<span class="leader"></span><span class="price">$10.99</span></div><p class="desc">mildly spiced chicken fritters</p></li>
    <li class="item"><div class="item-line">Fish Amritsari<span class="leader"></span><span class="price">$11.99</span></div><p class="desc">mildly spiced boneless fish fritters</p></li>
    <li class="item"><div class="item-line">Tawa Chicken<span class="leader"></span><span class="price">$12.99</span></div><p class="desc">barbeque chicken sauteed with bell pepper and onion cooked in chef special</p></li>
    <li class="item"><div class="item-line">Garlic Shrimp<span class="leader"></span><span class="price">$12.99</span></div><p class="desc">shrimp cooked in white wine and chef special garlic sauce</p></li>
    <li class="item"><div class="item-line">Spicy Wings<span class="leader"></span><span class="price">$0.00</span></div><p class="desc">8 pcs of hot spicy buffalo wings all time favorite</p></li>
    <li class="item"><div class="item-line">Tandoori Chicken<span class="leader"></span><span class="price">$7.99/$</span></div><p class="desc">chicken marinated in yogurt and mild spices cooked cooked in clay oven</p></li>
    <li class="item"><div class="item-line">Lemon Chicken<span class="leader"></span><span class="price">$0.00</span></div><p class="desc">chicken cooked with mild spices, lemon, and mango powder</p></li>
    <li class="item"><div class="item-line">Chicken Seekh Kabab<span class="leader"></span><span class="price">$9.50</span></div><p class="desc">ground chicken seasoned with fresh herbs and spices, rolled skewer</p></li>
    <li class="item"><div class="item-line">Lamb Seekh Kabab<span class="leader"></span><span class="price">$11.99</span></div><p class="desc">ground lamb seasoned with fresh herbs and spices, rolled skewer</p></li>
    <li class="item"><div class="item-line">Chicken Tikka<span class="leader"></span><span class="price">$10.50</span></div><p class="desc">boneless tender pieces of chicken seasoned with fresh herbs and yogurt cooked in clay oven</p></li>
    <li class="item"><div class="item-line">Chicken Malai Kabab<span class="leader"></span><span class="price">$10.99</span></div><p class="desc">boneless tender pieces of chicken marinated in sour cream</p></li>
    <li class="item"><div class="item-line">Achari Tikka<span class="leader"></span><span class="price">$10.99</span></div><p class="desc">boneless tender pieces of chicken marinated in pickle flavor sauce</p></li>
    <li class="item"><div class="item-line">Afghani Chicken<span class="leader"></span><span class="price">$12.99</span></div><p class="desc">mildly spiced chicken with savor cream cooked on a small fire</p></li>
    <li class="item"><div class="item-line">Fish Tikka Tandoori<span class="leader"></span><span class="price">$11.99</span></div><p class="desc">cubes of fish marinated in fresh herbs and ginger skewered in grill in tandoor</p></li>
    <li class="item"><div class="item-line">Salmon Fish<span class="leader"></span><span class="price">$13.50</span></div><p class="desc">cubes of salmon fish marinated in fresh herbs and ginger skewered and grilled in tandoor</p></li>
    <li class="item"><div class="item-line">Tawa Fish<span class="leader"></span><span class="price">$12.99</span></div><p class="desc">small piece of fish seasoned in yogurt and fresh herbs skewered and grilled in tandoor</p></li>
    <li class="item"><div class="item-line">Tandoori Shrimp<span class="leader"></span><span class="price">$14.99</span></div><p class="desc">6 pcs of jumbo shrimp marinated in yogurt, mild, spices and herb</p></li>
    <li class="item"><div class="item-line">Lamb Chop<span class="leader"></span><span class="price">$21.99</span></div><p class="desc">5 pcs of rack of lamb marinated in traditional herbs and roasted in a clay oven on skewers</p></li>
    <li class="item"><div class="item-line">Tandoori Mix Grill<span class="leader"></span><span class="price">$17.99</span></div><p class="desc">a delicious combination of grilled chicken, seekh kabab and shrimp</p></li>
  </ul>

  <h2 class="section-title" style="left:22px;width:348px;top:752px;">Vegetarian Appetizer</h2>
  <div class="divider" style="left:170px;top:799px;"></div>
  <ul class="menu-list" style="left:50px;width:296px;top:836px;--row:26px;">
    <li class="item"><div class="item-line">Vegetable Samosa<span class="leader"></span><span class="price">$2.99</span></div><p class="desc">2pcs of spicy seasoned potatoes &amp; peas wrapped in light pastry</p></li>
    <li class="item"><div class="item-line">Samosa Chaat<span class="leader"></span><span class="price">$7.49</span></div><p class="desc">2pcs of samosa served with chutney &amp; chholey</p></li>
    <li class="item"><div class="item-line">Aloo Tikki Chaat<span class="leader"></span><span class="price">$6.99</span></div><p class="desc">4pcs of aloo tikki served with chutney &amp; chholey</p></li>
    <li class="item"><div class="item-line">Mix Veg Pakora<span class="leader"></span><span class="price">$6.50</span></div><p class="desc">Deep fried vegetable fritters dipped in chick peas flour</p></li>
    <li class="item"><div class="item-line">Papri Chaat<span class="leader"></span><span class="price">$6.50</span></div><p class="desc">mixture of crisp flour crackers served with potato, chick peas, mint/tamarind sauce &amp; yogurt</p></li>
    <li class="item"><div class="item-line">Dahi Bhalla<span class="leader"></span><span class="price">$6.99</span></div><p class="desc">softball of mixed lentils topped with yogurt, mint, &amp; tamarind sauce</p></li>
    <li class="item"><div class="item-line">Paneer Pakora<span class="leader"></span><span class="price">$8.99</span></div><p class="desc">7 pcs of deep fried cottage cottage cheese fritters dipped in chick peas flour</p></li>
    <li class="item"><div class="item-line">Vegetable Seekh Kabab<span class="leader"></span><span class="price">$8.99</span></div><p class="desc">minced vegetable with cottage cheese seasoned with fresh herbs &amp; spices rolled skewers</p></li>
    <li class="item"><div class="item-line">Paneer Tikka Tandoori<span class="leader"></span><span class="price">$11.99</span></div><p class="desc">grilled paneer cheese, bell pepper, onion with a ginger flavor yogurt</p></li>
    <li class="item"><div class="item-line">Chhole Bhature<span class="leader"></span><span class="price">$9.99</span></div><p class="desc">2 pcs of large puffy shallow fried bread with served with chick peas</p></li>
    <li class="item"><div class="item-line">Stuffed Paneer Pakora<span class="leader"></span><span class="price">$8.50</span></div><p class="desc">6 pcs of homemade cheese stuffed with mixture of delicious spiced potato &amp; mint</p></li>
    <li class="item"><div class="item-line">Chatpati Aloo Chaat<span class="leader"></span><span class="price">$7.50</span></div></li>
  </ul>

  <!-- Middle panel -->
  <h2 class="section-title" style="left:382px;width:381px;top:96px;">Soup, Salad, &amp; Raita</h2>
  <div class="divider" style="left:546px;top:142px;"></div>
  <ul class="menu-list" style="left:432px;width:290px;top:168px;">
    <li class="item" style="--row:25px;"><div class="item-line">Tomato Soup<span class="leader"></span><span class="price">$3.99</span></div><p class="desc">a simple soup made with fresh tomato</p></li>
    <li class="item" style="--row:25px;"><div class="item-line">Vegetarian Soup<span class="leader"></span><span class="price">$3.99</span></div><p class="desc">a soup made with variety of vegetables</p></li>
    <li class="item" style="--row:25px;"><div class="item-line">Chicken Soup<span class="leader"></span><span class="price">$4.50</span></div><p class="desc">the classic chicken soup consist of a clear broth, served with small pieces of chicken</p></li>
    <li class="item" style="--row:25px;"><div class="item-line">Hot N Sour Soup<span class="leader"></span><span class="price">$4.99</span></div><p class="desc">a soup contains ingredients to make it both spicy and sour</p></li>
    <li class="item" style="--row:16px;"><div class="item-line">Fresh Garden Salad<span class="leader"></span><span class="price">$4.50</span></div></li>
    <li class="item" style="--row:16px;"><div class="item-line">Masala Salad<span class="leader"></span><span class="price">$5.99</span></div></li>
    <li class="item" style="--row:16px;"><div class="item-line">Mix Raita<span class="leader"></span><span class="price">$3.99</span></div></li>
    <li class="item" style="--row:16px;"><div class="item-line">Boondi Raita<span class="leader"></span><span class="price">$3.99</span></div></li>
    <li class="item" style="--row:16px;"><div class="item-line">Pudina Raita<span class="leader"></span><span class="price">$3.99</span></div></li>
    <li class="item" style="--row:16px;"><div class="item-line">Plain Dahi<span class="leader"></span><span class="price">$3.50</span></div></li>
  </ul>

  <div class="food-photo" role="img" aria-label="Photo of Indian dishes: rice biryani, curries and tandoori chicken in serving bowls"></div>

  <h2 class="section-title" style="left:382px;width:381px;top:780px;">Indo-Chinese</h2>
  <div class="divider" style="left:546px;top:827px;"></div>
  <ul class="menu-list" style="left:432px;width:290px;top:851px;--row:27.5px;">
    <li class="item"><div class="item-line">Chilli Paneer<span class="leader"></span><span class="price">$10.99</span></div><p class="desc">cottage cheese sauteed with bell pepper &amp; onion in Indian Chinese spicy sauce</p></li>
    <li class="item"><div class="item-line">Chilli Mushroom<span class="leader"></span><span class="price">$9.99</span></div><p class="desc">mushroom sauteed with bell pepper &amp; onion in Indian Chinese spicy sauce</p></li>
    <li class="item"><div class="item-line">Chilli Gobhi<span class="leader"></span><span class="price">$9.99</span></div><p class="desc">gobhi sauteed with bell pepper &amp; onion in Indian Chinese spicy sauce</p></li>
    <li class="item"><div class="item-line">Vegetable Manchurian<span class="leader"></span><span class="price">$10.50</span></div><p class="desc">mix vegetable ball cooked in chef special garlic sauce</p></li>
    <li class="item"><div class="item-line">Vegetable Chowmin<span class="leader"></span><span class="price">$8.30</span></div><p class="desc">stir fry noodles &amp; thin sliced vegetables cooked in Chinese sauce</p></li>
    <li class="item"><div class="item-line">Vegetable Spring Roll<span class="leader"></span><span class="price">$6.99</span></div><p class="desc">carrots, red bell pepper, bean sprouts, and bamboo shoots wrapped in spring rolls</p></li>
    <li class="item"><div class="item-line">Chilli Chicken<span class="leader"></span><span class="price">$10.99</span></div><p class="desc">boneless chicken sauteed with bell pepper and onion cooked in spicy cheese sauce</p></li>
    <li class="item"><div class="item-line">Chilli Fish<span class="leader"></span><span class="price">$13.99</span></div><p class="desc">fish fritters sauteed with bell pepper and onion cooked in spices</p></li>
    <li class="item"><div class="item-line">Chilli Shrimp<span class="leader"></span><span class="price">$12.99</span></div><p class="desc">shrimp with bell pepper and onion cooked in spicy cheese sauce</p></li>
    <li class="item"><div class="item-line">Chicken Manchurian<span class="leader"></span><span class="price">$10.99</span></div><p class="desc">chicken ball cooked in a semi thick garlic flavor Chinese sauce</p></li>
    <li class="item"><div class="item-line">Chicken Chowmin<span class="leader"></span><span class="price">$9.99</span></div><p class="desc">stir fry noodles and thin sliced vegetables with chicken cooked in Chinese sauce</p></li>
  </ul>

  <!-- Right panel -->
  <h2 class="section-title" style="left:763px;width:359px;top:96px;">Handi Sen (Non-Veg)</h2>
  <div class="divider" style="left:916px;top:142px;"></div>
  <ul class="menu-list" style="left:808px;width:280px;top:161px;--row:27.4px;">
    <li class="item"><div class="item-line">Chicken Makhni<span class="leader"></span><span class="price">$8.99</span></div><p class="desc">chicken pieces roasted in a clay oven &amp; then folded into a spiced tomato creamy sauce</p></li>
    <li class="item"><div class="item-line">Chicken Tikka Masala<span class="leader"></span><span class="price">$8.99</span></div><p class="desc">chunks of roasted chicken sauteed with bell pepper, onion folded into a spiced tomato sauce</p></li>
    <li class="item"><div class="item-line">Chicken Curry<span class="leader"></span><span class="price">$8.99</span></div><p class="desc">all time favorite chicken, fresh ginger, onion and tomato gravy</p></li>
    <li class="item"><div class="item-line">Chicken Korma<span class="leader"></span><span class="price">$8.99</span></div><p class="desc">boneless chicken cooked in a rich cashew and onion sauce</p></li>
    <li class="item"><div class="item-line">Kadai Chicken<span class="leader"></span><span class="price">$8.99</span></div><p class="desc">marinated chicken sauteed with bellpepper, onion and fresh tomato</p></li>
    <li class="item"><div class="item-line">Chicken Saag<span class="leader"></span><span class="price">$8.99</span></div><p class="desc">chicked cooked with fresh spinach</p></li>
    <li class="item"><div class="item-line">Chicken Jalfrezi<span class="leader"></span><span class="price">$8.99</span></div><p class="desc">grilled cubes of chicken breast sauteed with fresh vegetables</p></li>
    <li class="item"><div class="item-line">Chicken Masala<span class="leader"></span><span class="price">$8.99</span></div><p class="desc">savory chicken seasoned with chilli and lemon juice simmered in a sauce with exotic spices</p></li>
    <li class="item"><div class="item-line">Chicken Vindaloo<span class="leader"></span><span class="price">$8.99</span></div><p class="desc">cubes of chicken cooked with onion and potato in a very hot sauce</p></li>
    <li class="item"><div class="item-line">Goat Curry<span class="leader"></span><span class="price">$9.99</span></div><p class="desc">traditional Mughlai offering - a special blnd of baby goat on bones and spices</p></li>
    <li class="item"><div class="item-line">Goat Masala<span class="leader"></span><span class="price">$10.99</span></div><p class="desc">baby goat seasoned with chilli and lemon juice simmered in a sauce with exotic spices</p></li>
    <li class="item"><div class="item-line">Kadai Goat<span class="leader"></span><span class="price">$9.99</span></div><p class="desc">goat sauteed with bell pepper, onion and fresh tomato</p></li>
    <li class="item"><div class="item-line">Goat Saag<span class="leader"></span><span class="price">$9.99</span></div><p class="desc">boneless tender pieces of chicken marinated in pickle flavor sauce</p></li>
    <li class="item"><div class="item-line">Goat Vindaloo<span class="leader"></span><span class="price">$9.99</span></div><p class="desc">goat cooked with fresh spinach</p></li>
    <li class="item"><div class="item-line">Chicken Keema Mutter<span class="leader"></span><span class="price">$10.99</span></div><p class="desc">cooked with potato, vinegar and lots of hot red chilli peppers</p></li>
    <li class="item"><div class="item-line">Lamb Curry<span class="leader"></span><span class="price">$10.99</span></div><p class="desc">a classic dish from Northern India and amongst the most popular of all curries</p></li>
    <li class="item"><div class="item-line">Lamb Rogan Josh<span class="leader"></span><span class="price">$10.99</span></div><p class="desc">boneless lamb cooked in Kashmiri style</p></li>
    <li class="item"><div class="item-line">Lamb Saag<span class="leader"></span><span class="price">$10.99</span></div><p class="desc">lamb cooked with fresh spinach</p></li>
    <li class="item"><div class="item-line">Lamb Korma<span class="leader"></span><span class="price">$10.99</span></div><p class="desc">lamb cooked in light cream, almond and cashew nut sauce</p></li>
    <li class="item"><div class="item-line">Lamb Bhuna Ghost<span class="leader"></span><span class="price">$10.99</span></div><p class="desc">tender lamb cubes prepared with fresh ginger, onions, peppers, tomatoes and garlic</p></li>
    <li class="item"><div class="item-line">Lamb Vindaloo<span class="leader"></span><span class="price">$10.99</span></div><p class="desc">lamb cooked with potato, vinegar, and lots of hot red chilli peppers</p></li>
    <li class="item"><div class="item-line">Lamb Keema Mutter<span class="leader"></span><span class="price">$12.99</span></div><p class="desc">minced lamb cooked with peas , onions, tomatoes, herbs and spices</p></li>
  </ul>

  <h2 class="section-title" style="left:763px;width:359px;top:780px;">Seafood Special</h2>
  <div class="divider" style="left:916px;top:827px;"></div>
  <ul class="menu-list" style="left:808px;width:280px;top:851px;--row:27.5px;">
    <li class="item"><div class="item-line">Kadai Fish<span class="leader"></span><span class="price">$13.99</span></div><p class="desc">boneless fish sauteed with bell pepper, onion, and fresh tomato</p></li>
    <li class="item"><div class="item-line">Fish Curry<span class="leader"></span><span class="price">$13.99</span></div><p class="desc">a delicious fish curry which is both rich and aromatic</p></li>
    <li class="item"><div class="item-line">Fish Masala<span class="leader"></span><span class="price">$13.99</span></div><p class="desc">ajwain flavor fish cooked with fresh garlic and tomato</p></li>
    <li class="item"><div class="item-line">Goa Fish Curry<span class="leader"></span><span class="price">$12.59</span></div><p class="desc">fish curry made in this style is tangy and spicy</p></li>
    <li class="item"><div class="item-line">Fish Tikka Masala<span class="leader"></span><span class="price">$12.59</span></div><p class="desc">chunks of roasted fish in a rich read creamy lightly spiced tomato based sauce</p></li>
    <li class="item"><div class="item-line">Shrimp Curry<span class="leader"></span><span class="price">$12.99</span></div><p class="desc">cooked with fresh ginger, onion and tomato gravy</p></li>
    <li class="item"><div class="item-line">Shrimp Masala<span class="leader"></span><span class="price">$12.99</span></div><p class="desc">jumbo shrimp seasoned with chilli and lemon juice simmered in a sauce with exotic spices</p></li>
    <li class="item"><div class="item-line">Shrimp Saag<span class="leader"></span><span class="price">$12.99</span></div><p class="desc">shrimp cooked with fresh spinach</p></li>
    <li class="item"><div class="item-line">Shrimp Bhuna<span class="leader"></span><span class="price">$12.99</span></div><p class="desc">shrimp cooked with shredded onions, green peppers, and spices</p></li>
    <li class="item"><div class="item-line">Shrimp Vindaloo<span class="leader"></span><span class="price">$12.99</span></div><p class="desc">shrimp cooked with potato, vinegar, and lots of hot red chilli peppers</p></li>
    <li class="item"><div class="item-line">Kadai Shrimp<span class="leader"></span><span class="price">$12.99</span></div><p class="desc">shrimp sauteed with ginger, onion, fresh tomatoes, and oriental spices</p></li>
  </ul>
</main>
</body>
</html>
```